Corvale Motorized Shade Business Card

Hello, we've had our logo made. Now we are looking for a clean and cool looking business card. One side can just be the logo with any design elements that might look good with it. The other side will be Name, Phone Number and Email. There will not be an address on the card.

```html
<!DOCTYPE html>
<html lang="en">
<head>
<meta charset="utf-8">
<title>Corvale Motorized Shade – Business Card</title>
<link rel="stylesheet" href="https://fonts.googleapis.com/css2?family=Bebas+Neue&family=Montserrat:wght@700&family=Noto+Sans:wght@400&display=swap">
<style>
  :root {
    --navy: #22446f;
    --navy-edge: #1b2f4a;
    --sky: #0aa0e0;
    --sun: #fcc400;
    --paper: #fdfdfd;
  }
  html, body {
    margin: 0;
    padding: 0;
    width: 1200px;
    height: 1200px;
    overflow: hidden;
    background: var(--paper);
  }
  .canvas {
    position: relative;
    width: 1200px;
    height: 1200px;
  }
  .card {
    position: absolute;
    left: 324px;
    width: 560px;
    height: 320px;
    background: var(--navy);
    border: 1px solid var(--navy-edge);
    box-sizing: border-box;
    overflow: hidden;
  }
  .card--front { top: 276px; }
  .card--back { top: 611px; }

  .brand-disc {
    position: absolute;
    left: 152px;
    top: 32px;
    width: 256px;
    height: 256px;
    border-radius: 50%;
    background: var(--paper);
    display: flex;
    flex-direction: column;
    align-items: center;
    justify-content: center;
  }
  .brand-name {
    font-family: "Montserrat", sans-serif;
    font-weight: 700;
    color: var(--navy);
    text-align: center;
    margin: 0;
    line-height: 1.1;
  }
  .brand-name__main {
    display: block;
    font-size: 34px;
    letter-spacing: 1px;
  }
  .brand-name__sub {
    display: block;
    font-size: 9.5px;
    letter-spacing: 3px;
    margin-top: 6px;
  }

  .person-name {
    position: absolute;
    left: 84px;
    top: 80px;
    margin: 0;
    font-family: "Bebas Neue", sans-serif;
    font-size: 43px;
    line-height: 1;
    color: var(--sun);
  }
  .person-role {
    position: absolute;
    left: 84px;
    top: 122px;
    margin: 0;
    font-family: "Montserrat", sans-serif;
    font-weight: 700;
    font-size: 16px;
    letter-spacing: -0.3px;
    color: var(--sun);
  }
  .divider {
    position: absolute;
    left: 84px;
    top: 154px;
    width: 324px;
    height: 1px;
    background: var(--sun);
    opacity: 0.8;
  }
  .contact-rule {
    position: absolute;
    left: 143px;
    top: 182px;
    width: 1px;
    height: 72px;
    background: var(--sun);
  }
  .contact-icon {
    position: absolute;
    left: 85px;
    width: 32px;
    height: 32px;
  }
  .contact-icon--phone { top: 182px; }
  .contact-icon--mail { top: 222px; }
  .contact-text {
    position: absolute;
    left: 182px;
    margin: 0;
    font-family: "Noto Sans", sans-serif;
    font-weight: 400;
    font-size: 20px;
    line-height: 1;
    color: var(--sun);
  }
  .contact-text--phone { top: 187px; }
  .contact-text--mail { top: 228px; }
</style>
</head>
<body>
<main class="canvas">
  <section class="card card--front" aria-label="Card front">
    <div class="brand-disc">
      <p class="brand-name">
        <span class="brand-name__main">CORVALE</span>
        <span class="brand-name__sub">MOTORIZED SHADE</span>
      </p>
    </div>
  </section>

  <section class="card card--back" aria-label="Card back">
    <h1 class="person-name">NAME</h1>
    <p class="person-role">DESIGNATION</p>
    <div class="divider"></div>

    <svg class="contact-icon contact-icon--phone" viewBox="0 0 32 32" aria-hidden="true">
      <circle cx="16" cy="16" r="16" fill="var(--sky)"/>
      <path d="M10.5 9.2c.6-.6 1.4-.5 1.8.1l1.3 2c.3.5.2 1.1-.2 1.5l-.8.7c.8 1.8 2.2 3.3 4 4.1l.7-.8c.4-.4 1-.5 1.5-.2l2 1.3c.6.4.7 1.2.1 1.8l-.9.9c-.9.9-2.2 1-3.4.4-3-1.5-5.4-3.9-6.9-6.9-.6-1.2-.5-2.5.4-3.4z" fill="none" stroke="var(--navy)" stroke-width="1.6" stroke-linejoin="round"/>
    </svg>
    <svg class="contact-icon contact-icon--mail" viewBox="0 0 32 32" aria-hidden="true">
      <circle cx="16" cy="16" r="16" fill="var(--sky)"/>
      <rect x="7.5" y="10" width="17" height="12" fill="none" stroke="var(--navy)" stroke-width="1.4"/>
      <path d="M7.5 10l8.5 7 8.5-7M7.5 22l6-5.5M24.5 22l-6-5.5" fill="none" stroke="var(--navy)" stroke-width="1.4"/>
    </svg>
    <div class="contact-rule"></div>

    <p class="contact-text contact-text--phone">25730 26081</p>
    <p class="contact-text contact-text--mail">XXXX@CORVALE.COM</p>
  </section>
</main>
</body>
</html>
```